Heavy Rock band needs EP cover

Hello! We are a heavy rock band from Montana who needs an album cover for our new EP that we will be releasing sometime this year.
We would love something that revolves around nature, I was thinking specifically a forest because the song that shares the album name has a chorus that goes as follows:
It’s like a dream guided to the forest
I’m wasting breath and I’m out of time
Another push or else i’ve fallen out of line
It’s like I’m sick, guide me to the forest
You help me find my way,
An endless stream, it never was a sight to see
It’s like I’m stuck guide me to the forest
The whole tone is a little dark, perhaps a darker design with some color splashes or specific objects of focus in color.
Some random images that come to mind that you can use (or not) for this project:
a. A path leading into a forest
b. A cabin the middle of a forest as a focal point
c. A person at the edge of a forest or edge of a path
Something like that! Im trying to portray the forest as more of a force in and of itself so whatever techniques you want to use to portray that.
I created an album cover that I wanted to use before for this project, but we ended up using that template on the print version of our last CD's, unfortunately. I've attached that cover to the files, it's the pink one. The one with the mountains was our last album cover, which is unrelated i suppose.
The only other thing I can think of is if you want to put a modern spin on it with different patterns, lines or geometric shapes that could be cool! But I’m not a graphic designer so what do I know. Strait up old school could be cool too.
We only need a front cover this time because I don't know if we are going to necessarily print physical copies of it.
Here is the info for our present day album:
Title: Tethered
Band Name: Nine Pebble Hallway
I've attached our logo if you want to use it, but if you want to create a new one or just use our band name in whatever font you want, it's fine with us.

```html
<!DOCTYPE html>
<html lang="en">
<head>
<meta charset="utf-8">
<title>Tethered — Nine Pebble Hallway EP Cover</title>
<link rel="stylesheet" href="https://fonts.googleapis.com/css2?family=Fredoka:wght@700&family=Montserrat:wght@700&display=swap">
<style>
  :root {
    --canvas-bg: #474850;
    --forest-deep: #1c1418;
    --forest-green: #2f3b26;
    --forest-moss: #4d5a2c;
    --foliage-gold: #b9a244;
    --path-rust: #6b3a26;
    --title-cream: #f6d784;
    --title-rust: #7a3a17;
    --band-white: #ffffff;
  }
  * { margin: 0; padding: 0; box-sizing: border-box; }
  html, body {
    width: 1200px;
    height: 826px;
    overflow: hidden;
    background: var(--canvas-bg);
  }
  .canvas {
    position: relative;
    width: 1200px;
    height: 826px;
  }
  .cover {
    position: absolute;
    left: 230px;
    top: 43px;
    width: 740px;
    height: 740px;
    overflow: hidden;
    box-shadow: 0 6px 18px rgba(0, 0, 0, 0.35);
  }
  .cover-photo {
    position: absolute;
    inset: 0;
    background:
      radial-gradient(ellipse 40% 30% at 62% 72%, rgba(107, 58, 38, 0.75), transparent 70%),
      radial-gradient(ellipse 35% 40% at 92% 88%, rgba(185, 162, 68, 0.7), transparent 70%),
      radial-gradient(ellipse 30% 35% at 38% 30%, rgba(77, 90, 44, 0.7), transparent 70%),
      linear-gradient(180deg, var(--forest-green) 0%, var(--forest-moss) 45%, var(--forest-deep) 100%);
  }
  .cover-photo::after {
    content: "";
    position: absolute;
    inset: 0;
    background: linear-gradient(90deg, rgba(28, 20, 24, 0.85) 0%, rgba(28, 20, 24, 0) 35%);
  }
  .ep-title {
    position: absolute;
    left: 86px;
    top: 376px;
    transform: translate(-50%, -50%) rotate(-90deg);
    font-family: "Fredoka", "Arial Rounded MT Bold", sans-serif;
    font-weight: 700;
    font-size: 96px;
    line-height: 1;
    letter-spacing: 8px;
    color: var(--title-cream);
    -webkit-text-stroke: 3px var(--title-rust);
    paint-order: stroke fill;
    white-space: nowrap;
    text-transform: uppercase;
  }
  .band-mark {
    position: absolute;
    left: 619px;
    top: 36px;
    width: 64px;
    height: 64px;
    border: 3px solid var(--band-white);
  }
  .band-name {
    position: absolute;
    left: 651px;
    top: 114px;
    transform: translateX(-50%);
    font-family: "Montserrat", "Helvetica Neue", sans-serif;
    font-weight: 700;
    font-size: 13px;
    line-height: 17px;
    letter-spacing: 0.32em;
    color: var(--band-white);
    text-align: center;
    white-space: nowrap;
    text-transform: uppercase;
  }
</style>
</head>
<body>
  <main class="canvas">
    <section class="cover">
      <div class="cover-photo" role="img" aria-label="Dark forest photograph: a hiker in a red beanie and green backpack walks a rooty dirt path toward a weathered wooden cabin among tall pines, with golden foliage in the foreground"></div>
      <h1 class="ep-title">Tethered</h1>
      <div class="band-mark" aria-hidden="true"></div>
      <p class="band-name">Nine Pebble<br>Hallway</p>
    </section>
  </main>
</body>
</html>
```